Kelvora Ledger Web Design Contest

We would like for you to design a website for www.kelvoraledger-example.com. Kelvora Ledger is a CPA Firm offering accounting, auditing, and tax preparation services.

We would like to have a consistent feel with the logo, business card, envelope, and stationary designs that were created by another designer on PlanHive. Examples of each are attached. We would like the website to have a clean/modern style.

The website should include the following:

1. A general "Welcome" landing page
2. A "About the Company" page
3. A "Services Offered" page
4. A "Contact Us" form
5. A button for "Sign up for Newsletter"

Target Market(s)

Individuals and businesses that require accounting, auditing, and tax preparation services from a CPA.

Industry/Entity Type

Accounting

Coding

Number of Pages Required

5+ page

Font styles to use
Other font styles liked:
• Trebuchet or similar

Requirements
Must have
• Consistent feel with logo and letterhead. The gray and blue bar on the letterhead should be incorporated into the website design.

```html
<!DOCTYPE html>
<html lang="en">
<head>
<meta charset="UTF-8">
<title>Kelvora Ledger — Home</title>
<link rel="stylesheet" href="https://fonts.googleapis.com/css2?family=Arimo:wght@400;700&family=Questrial&display=swap">
<style>
  :root {
    --navy: #04236f;
    --charcoal: #4d4d4d;
    --button-gray: #8a8a8a;
    --ink: #111111;
    --white: #ffffff;
    --band: #e6e6ea;
    --hero-light: #dfe7f1;
    --hero-mid: #b9c8da;
    --hero-deep: #8fa3bd;
  }
  * { margin: 0; padding: 0; box-sizing: border-box; }
  html, body { width: 1079px; height: 1200px; overflow: hidden; background: var(--white); }
  body { position: relative; font-family: "Arimo", Arial, sans-serif; color: var(--ink); }

  .header-shapes, .footer-shapes { position: absolute; left: 0; width: 1079px; }
  .header-shapes { top: 0; height: 180px; }
  .footer-shapes { top: 1140px; height: 60px; }

  .brand { position: absolute; left: 10px; top: 40px; width: 330px; text-align: center; }
  .brand-mark { width: 64px; height: 64px; border: 3px solid var(--charcoal); margin: 0 auto 14px; }
  .brand-name { font-family: "Arimo", Arial, sans-serif; font-weight: 700; font-size: 20px; color: var(--navy); letter-spacing: 0.5px; }
  .brand-tagline { margin-top: 5px; font-family: "Arimo", Arial, sans-serif; font-size: 13px; letter-spacing: 1.2px; color: var(--charcoal); }

  .newsletter-btn { position: absolute; left: 873px; top: 29px; width: 171px; height: 24px; background: var(--button-gray); color: var(--white); font-size: 13.5px; line-height: 24px; text-align: center; border-radius: 2px; }

  .main-nav { position: absolute; top: 140px; left: 0; width: 1079px; height: 26px; }
  .main-nav a { position: absolute; font-family: "Questrial", "Century Gothic", sans-serif; font-size: 19.5px; color: var(--white); text-decoration: none; }

  .hero { position: absolute; left: 0; top: 212px; width: 1079px; height: 400px;
    background: linear-gradient(115deg, var(--hero-light) 0%, var(--hero-mid) 45%, var(--hero-light) 70%, var(--hero-deep) 100%); }
  .hero-band { position: absolute; left: 0; top: 612px; width: 1079px; height: 14px; background: var(--band); }
  .hero-panel { position: absolute; left: 212px; top: 120px; width: 646px; height: 186px; background: rgba(255,255,255,0.72); text-align: center; }
  .hero-title { margin-top: 30px; font-size: 17.5px; font-weight: 400; }
  .hero-text { margin-top: 8px; font-size: 15px; line-height: 21.5px; }
  .hero-btn { display: inline-block; margin-top: 14px; width: 113px; height: 24px; line-height: 24px; background: var(--navy); color: var(--white); font-size: 13.5px; }
  .hero-arrow { position: absolute; top: 165px; width: 40px; height: 84px; }
  .hero-arrow.prev { left: 34px; }
  .hero-arrow.next { left: 1006px; }

  .service { position: absolute; top: 696px; width: 300px; text-align: center; }
  .service-photo { width: 170px; height: 170px; border-radius: 50%; margin: 0 auto; }
  .service-title { font-size: 17.5px; font-weight: 400; margin-top: 27px; }
  .service-text { margin-top: 16px; font-size: 15px; line-height: 21.2px; }

  .copyright { position: absolute; left: 156px; top: 1170px; font-size: 14.5px; color: var(--white); }
  .social { position: absolute; top: 1160px; width: 20px; height: 20px; border-radius: 50%; background: var(--white); }
</style>
</head>
<body>

<svg class="header-shapes" viewBox="0 0 1079 180" aria-hidden="true">
  <polygon points="0,0 504,0 486,20 0,20" fill="var(--navy)"/>
  <polygon points="545,0 1079,0 1079,178 384,178" fill="var(--charcoal)"/>
</svg>

<div class="brand">
  <div class="brand-mark"></div>
  <div class="brand-name">KELVORA LEDGER, LLC</div>
  <div class="brand-tagline">Accounting · Audit · Tax Services</div>
</div>

<div class="newsletter-btn">Sign up for Newsletter</div>

<nav class="main-nav">
  <a href="#" style="left:483px">HOME</a>
  <a href="#" style="left:618px">About Us</a>
  <a href="#" style="left:768px">Services</a>
  <a href="#" style="left:919px">Contact Us</a>
</nav>

<section class="hero" role="img" aria-label="Calculator, coins and financial printouts in soft blue tones">
  <svg class="hero-arrow prev" viewBox="0 0 40 84" aria-hidden="true"><polyline points="36,2 2,42 36,82" fill="none" stroke="#fff" stroke-width="1.5"/></svg>
  <svg class="hero-arrow next" viewBox="0 0 40 84" aria-hidden="true"><polyline points="4,2 38,42 4,82" fill="none" stroke="#fff" stroke-width="1.5"/></svg>
  <div class="hero-panel">
    <h2 class="hero-title">Tax preparation services</h2>
    <p class="hero-text">Nunc ac magna. Maecenas odio dolor, vulputate vel, auctor ac, accumsan id,<br>felis. Pellentesque cursus sagittis felis. Pellentesque porttitor, velit lacinia<br>egestas auctor, diam eros tempus arcu, nec vulputate augue magna vel risus.</p>
    <span class="hero-btn">Learn More...</span>
  </div>
</section>
<div class="hero-band"></div>

<article class="service" style="left:66px">
  <div class="service-photo" role="img" aria-label="Close-up of calculator keys" style="background:radial-gradient(circle at 40% 40%, #c9d6e2, #5d7489)"></div>
  <h3 class="service-title">Tax preparation services</h3>
  <p class="service-text">Nunc ac magna. Maecenas odio dolor,<br>vulputate vel, auctor ac, accumsan id,<br>felis. Pellentesque cursus sagittis felis.<br>Pellentesque porttitor, velit lacinia eges-<br>tas auctor, diam eros tempus arcu, nec<br>vulputate augue magna vel risus.</p>
</article>

<article class="service" style="left:384px">
  <div class="service-photo" role="img" aria-label="Printed business charts with a pen" style="background:linear-gradient(160deg, #3a3f5a 0%, #e9ecef 40%, #f2f2f2 60%, #6a5ac0 85%, #e85a2a 100%)"></div>
  <h3 class="service-title">Accounting</h3>
  <p class="service-text">Nunc ac magna. Maecenas odio dolor,<br>vulputate vel, auctor ac, accumsan id,<br>felis. Pellentesque cursus sagittis felis.<br>Pellentesque porttitor, velit lacinia eges-<br>tas auctor, diam eros tempus arcu, nec<br>vulputate augue magna vel risus.</p>
</article>

<article class="service" style="left:694px">
  <div class="service-photo" role="img" aria-label="Hands reviewing documents beside a keyboard" style="background:linear-gradient(135deg, #2c2c2c 0%, #e7e2dc 35%, #f4f4f4 60%, #3a3a3a 100%)"></div>
  <h3 class="service-title">Auditing</h3>
  <p class="service-text">Nunc ac magna. Maecenas odio dolor,<br>vulputate vel, auctor ac, accumsan id,<br>felis. Pellentesque cursus sagittis felis.<br>Pellentesque porttitor, velit lacinia eges-<br>tas auctor, diam eros tempus arcu, nec<br>vulputate augue magna vel risus.</p>
</article>

<svg class="footer-shapes" viewBox="0 0 1079 60" aria-hidden="true">
  <polygon points="0,14 628,14 592,58 0,58" fill="var(--navy)"/>
  <polygon points="656,2 1079,2 1079,58 608,58" fill="var(--charcoal)"/>
</svg>

<div class="copyright">Copyright © 2015 Kelvora Ledger</div>
<span class="social" style="left:800px"></span>
<span class="social" style="left:849px"></span>
<span class="social" style="left:900px"></span>
<span class="social" style="left:950px"></span>

</body>
</html>
```